Slide Template Design - For Professional Powerpoint Presentation

Hello, this competition is to design one or more PowerPoint slides using the template provided as a base.

This presentation will be used by my business - to provide REPORTS (with lots of content on each slide) on investments to clients.

It is possible to win this competition by just designing 1 slide - the "Typical Slide (with Text)" is the most important.

The slides I would like are:
- Cover Page Template
- Table of Contents Template
- Section Divider Template
- Typical Slide (with Text)

The presentation should look clean, clear, highly professional, and use mainly black, grey, white colours. One colour may (but does not have to) feature as a design element.

The design is what I am most interested in - the text can be pasted in.

I do not need a logo (I already have on in black and white).

```html
<!DOCTYPE html>
<html lang="en">
<head>
<meta charset="UTF-8">
<title>Cover Slide – Presentation Title</title>
<link rel="stylesheet" href="https://fonts.googleapis.com/css2?family=Abril+Fatface&family=Libre+Caslon+Text&family=Montserrat:wght@500;700&family=Open+Sans:wght@400;600&display=swap">
<style>
  :root {
    --ink: #000000;
    --panel: rgba(28, 28, 28, 0.86);
    --white: #ffffff;
    --rule: rgba(255, 255, 255, 0.85);
    --frame: rgba(200, 200, 200, 0.9);
    --tag-fill: rgba(255, 255, 255, 0.35);
    --tag-ink: #2f2f2f;
    --date-ink: #333333;
  }
  html, body {
    margin: 0;
    padding: 0;
    overflow: hidden;
    background: #ffffff;
  }
  .slide {
    position: relative;
    width: 1200px;
    height: 900px;
    overflow: hidden;
  }
  .backdrop {
    position: absolute;
    inset: 0;
    background:
      radial-gradient(ellipse 420px 300px at 120px 760px, rgba(70, 70, 72, 0.75), rgba(70, 70, 72, 0) 70%),
      radial-gradient(ellipse 260px 200px at 1000px 420px, rgba(90, 90, 95, 0.35), rgba(90, 90, 95, 0) 70%),
      linear-gradient(180deg, #e9e8e6 0%, #d9d8d6 30%, #cfcecd 55%, #dedddb 80%, #e8e7e5 100%);
  }
  .guide {
    position: absolute;
    background: var(--rule);
  }
  .guide--vertical { left: 181px; top: 0; width: 2px; height: 900px; }
  .guide--left { left: 0; top: 777px; width: 473px; height: 2px; }
  .guide--right { left: 1109px; top: 777px; width: 91px; height: 2px; }

  .date-tab {
    position: absolute;
    left: 149px;
    top: 91px;
    width: 58px;
    height: 426px;
    border: 1.5px solid var(--frame);
    display: flex;
    align-items: center;
    justify-content: center;
  }
  .date-tab__text {
    transform: rotate(-90deg);
    white-space: nowrap;
    font-family: "Montserrat", sans-serif;
    font-weight: 500;
    font-size: 23px;
    letter-spacing: 6px;
    color: var(--date-ink);
  }

  .logo-block {
    position: absolute;
    left: 408px;
    top: 36px;
    width: 377px;
    height: 155px;
    background: var(--ink);
    color: var(--white);
    font-family: "Open Sans", sans-serif;
    text-align: center;
    display: flex;
    flex-direction: column;
    justify-content: center;
    gap: 2px;
  }
  .logo-block__label { font-size: 24px; line-height: 1.25; }
  .logo-block__note { font-size: 39px; font-weight: 600; line-height: 1.2; }
  .logo-block__suffix { font-size: 24px; line-height: 1.25; }

  .panel {
    position: absolute;
    left: 408px;
    width: 548px;
    background: var(--panel);
    color: var(--white);
    text-align: center;
    display: flex;
    align-items: center;
    justify-content: center;
  }
  .panel--title { top: 216px; height: 213px; }
  .panel--description { top: 451px; height: 212px; }
  .panel__title {
    margin: 0;
    font-family: "Abril Fatface", serif;
    font-weight: 400;
    font-size: 64px;
    line-height: 1.38;
    letter-spacing: 1px;
  }
  .panel__description {
    margin: 0;
    font-family: "Libre Caslon Text", serif;
    font-size: 40px;
    line-height: 1.45;
    padding-bottom: 34px;
  }

  .tagline {
    position: absolute;
    left: 473px;
    top: 749px;
    width: 636px;
    height: 63px;
    box-sizing: border-box;
    border: 1.5px solid var(--frame);
    background: var(--tag-fill);
    display: flex;
    align-items: center;
    justify-content: center;
    font-family: "Montserrat", sans-serif;
    font-weight: 700;
    font-size: 22px;
    letter-spacing: 3.5px;
    text-transform: uppercase;
    color: var(--tag-ink);
  }
</style>
</head>
<body>
  <main class="slide">
    <div class="backdrop" role="img" aria-label="Photograph of a person at a white wooden desk holding a smartphone, with a notebook, a cup of coffee and a second phone on the table"></div>

    <div class="guide guide--vertical"></div>
    <div class="guide guide--left"></div>
    <div class="guide guide--right"></div>

    <div class="date-tab">
      <span class="date-tab__text">14 / 10 / 2019</span>
    </div>

    <div class="logo-block">
      <span class="logo-block__label">Logo</span>
      <span class="logo-block__note">(do not design)</span>
      <span class="logo-block__suffix">Pty Ltd</span>
    </div>

    <section class="panel panel--title">
      <h1 class="panel__title">Presentation<br>Title</h1>
    </section>

    <section class="panel panel--description">
      <p class="panel__description">Presentation<br>Description</p>
    </section>

    <div class="tagline">Company tag line goes hearc</div>
  </main>
</body>
</html>
```